Tour operator needs simple coded WordPress site (updated extra payment for coding and guaranteed)

[update 9/7/2015]
If you design a new logo and it gets accepted, even if we use another template with your logo you will get $50
[update 8/7/2015]
Update on questions about dual-language
For dual languages we are happy to set up a second site with the same designs in a second language.
For the design aspect just allow the user to switch between languages with an icon.
For the coding, a replica of the site on a second server will do (to save messing around with multiple language plugins) - we will populate it with Chinese text
[original post]
Simple coded WordPress site for tours
You can choose to design only or design and code ($340 design, $150 bonus for coding)
Open design brief - use your creativity
Will be in 2 languages (English and Chinese) but design needs only to be in one language
Winning design will be chosen only from home page, but the winner must make a second standard template page when chosen at no extra cost.
Must be responsive design
We only need homepage and standard template page design and coding, we will populate the pages
You can use design ideas from our pamphlet if you like - attached
Only a sample logo and colors on website and pamphlet - feel free to change as the current ones seem restrictive
Current website framework only to give an idea of the number of pages and basic menu structure (no need to use existing navigation style or any style at all for that matter, open brief)
http://brightwaterlearningtrips.com.au/
Target Market(s)
Chinese parents of kids 10-14 (the kids will take the tour)
Industry/Entity Type
Tour
Number of Pages Required
2 page
Look and feel
Each slider illustrates characteristics of the customer's brand and the style your logo design should communicate.

```html
<!DOCTYPE html>
<html lang="en">
<head>
<meta charset="utf-8">
<title>Brightwater Learning Trips – Home</title>
<link href="https://fonts.googleapis.com/css2?family=Open+Sans:wght@400;600;700&family=Raleway:wght@400;500;700&display=swap" rel="stylesheet">
<style>
:root{
  --navy:#1d2a55;
  --navy-dark:#141d3d;
  --orange:#f4a31c;
  --orange-dark:#e08d0a;
  --teal:#2b8a9c;
  --ink:#333;
  --muted:#777;
  --paper:#fff;
  --panel:#f1f1f1;
  --footer:#151515;
  --footer-line:#2a2a2a;
  --sky:#dcecf5;
}
*{box-sizing:border-box;margin:0;padding:0}
html,body{width:1200px;height:2284px;overflow:hidden}
body{font-family:"Open Sans",Arial,sans-serif;color:var(--ink);background:var(--panel);position:relative}
.backdrop{position:absolute;left:0;top:0;width:1200px;height:1160px;background:linear-gradient(180deg,#5fa9c9 0%,#7cc3d4 30%,#4aa1a8 60%,#2f7f8a 100%)}
.page{position:relative;width:1200px;height:2284px}

/* top bar */
.topbar{position:absolute;left:140px;top:16px;width:920px;height:80px}
.brand{position:absolute;left:0;top:8px;display:flex;align-items:center;gap:10px}
.brand-mark{width:46px;height:46px;border-radius:50%;background:var(--navy)}
.brand-name{font-family:"Open Sans",sans-serif;font-weight:700;font-size:22px;color:var(--navy)}
.social{position:absolute;left:470px;top:30px;display:flex;gap:8px}
.social span{width:22px;height:22px;border-radius:50%;background:#2c2c2c;display:block}
.lang{position:absolute;right:0;top:32px;display:flex;align-items:center;gap:10px;font-size:12px;color:#1b1b1b}
.flag{width:20px;height:13px;display:block}
.flag.en{background:#fff;border:1px solid #ccc}
.flag.cn{background:#d72a1e}

/* nav */
.nav{position:absolute;left:140px;top:108px;width:920px;height:32px;background:var(--navy);display:flex;align-items:center;padding-left:14px}
.nav a{color:#fff;font-size:11px;font-weight:600;letter-spacing:.5px;text-decoration:none;margin-right:30px}
.nav .auth{margin-left:auto;display:flex;height:100%}
.nav .auth a{margin:0;padding:0 16px;display:flex;align-items:center}
.nav .login{background:var(--orange)}
.nav .register{background:var(--navy-dark)}

/* hero */
.hero{position:absolute;left:140px;top:150px;width:920px;height:455px;background:#fff;padding:10px}
.hero-photo{width:100%;height:100%;background:linear-gradient(180deg,#8fc4e6 0%,#b9d9ec 45%,#d9c7a0 70%,#3d6f8f 100%)}
.hero-banner{position:absolute;left:10px;top:232px;width:330px;height:88px;background:rgba(43,138,156,.88);border:2px solid rgba(255,255,255,.7);padding:14px 18px;font-family:"Raleway",sans-serif;font-weight:700;font-size:26px;color:#fff;line-height:1.15;letter-spacing:.5px}

/* intro */
.intro{position:absolute;left:140px;top:610px;width:920px;height:455px;background:var(--paper);padding:34px 26px 0;text-align:center}
.intro h1{font-family:"Raleway",sans-serif;font-weight:500;font-size:34px;color:var(--navy);letter-spacing:1px;margin-bottom:14px}
.intro h1 em{font-style:normal;color:var(--orange)}
.intro p{font-size:12px;line-height:1.7;color:#555;margin-bottom:16px;text-align:left}
.btn{display:inline-block;background:var(--orange);color:#fff;font-size:12px;font-weight:600;text-decoration:none}
.intro .btn{padding:12px 44px;margin-top:14px}

/* explore */
.explore{position:absolute;left:140px;top:1070px;width:920px;height:400px;background:linear-gradient(180deg,var(--sky),#eef6fa);text-align:center;padding-top:40px}
.explore h2{font-family:"Raleway",sans-serif;font-weight:500;font-size:22px;color:#333;letter-spacing:1px}
.explore .lead{font-size:10px;color:var(--muted);margin-top:12px}
.trips{position:absolute;left:32px;top:150px;display:flex;gap:28px}
.trip{position:relative;width:265px;height:220px;background:#fff;padding:5px}
.trip .photo{width:100%;height:100%}
.trip .label{position:absolute;left:5px;bottom:32px;background:rgba(20,29,61,.8);color:#fff;font-size:13px;font-weight:600;padding:8px 16px}
.trip .badge{position:absolute;right:14px;bottom:22px;width:50px;height:50px;border-radius:50%;background:var(--orange);color:#fff;font-size:9px;font-weight:700;display:flex;align-items:center;justify-content:center;text-align:center;line-height:1.1}

/* offers */
.offers{position:absolute;left:140px;top:1490px;width:920px;height:380px;background:var(--paper);padding:22px 20px}
.offers h3{font-family:"Raleway",sans-serif;font-weight:700;font-size:16px;color:var(--navy);border-bottom:2px solid var(--orange);display:inline-block;padding-bottom:4px}
.col-title{position:absolute;top:72px;font-size:11px;font-weight:600;color:#333}
.sponsored{position:absolute;left:20px;top:96px;width:210px}
.sponsored .photo{height:220px;background:linear-gradient(180deg,#8cc3ea,#9fc1a0 60%,#5b7d45)}
.sponsored .btn{margin-top:14px;padding:6px 16px;font-size:10px}
.specials{position:absolute;left:268px;top:96px;display:flex;gap:18px}
.card{width:196px;height:250px;border:1px solid #e2e2e2;padding:10px;text-align:center}
.card .thumb{width:120px;height:90px;margin:0 auto;border-radius:6px}
.card h4{font-size:11px;font-weight:700;color:#d9472b;margin:12px 0 6px}
.card p{font-size:8.5px;color:var(--muted);line-height:1.55}
.card .btn{margin-top:12px;padding:6px 14px;font-size:9px}

/* footer */
.footer{position:absolute;left:0;top:1900px;width:1200px;height:384px;background:var(--footer)}
.links{position:absolute;left:205px;top:82px;display:grid;grid-template-columns:150px 150px;row-gap:10px}
.links a{color:#ddd;font-size:9.5px;text-decoration:none;letter-spacing:.4px}
.follow{position:absolute;left:600px;top:84px;width:140px}
.follow .title{display:block;color:var(--orange);font-size:14px;font-weight:600;margin-bottom:14px}
.follow .icons{display:flex;gap:8px}
.follow .icons span{width:22px;height:22px;background:#e8e8e8;display:block}
.footer-brand{position:absolute;left:880px;top:96px;display:flex;align-items:center;gap:10px}
.footer-brand .brand-mark{background:#888}
.footer-brand .brand-name{color:#eee;font-size:20px}
.copyright{position:absolute;left:0;top:280px;width:1200px;border-top:1px solid var(--footer-line);padding-top:10px;text-align:center;font-size:8.5px;color:#888;letter-spacing:.5px}
.promo{position:absolute;left:180px;top:316px;width:840px;height:56px;background:linear-gradient(180deg,#2a2a2a,#0e0e0e);display:flex;align-items:center;padding:0 16px;gap:16px}
.promo .download{background:var(--orange);color:#111;font-weight:700;font-size:14px;padding:8px 22px}
.promo .item{margin-left:36px;color:#f1c230;font-size:10px;font-weight:700;line-height:1.3}
.promo .item small{display:block;color:#bbb;font-weight:400;font-size:8px}
</style>
</head>
<body>
<div class="page">
  <div class="backdrop" role="img" aria-label="Tropical beach with turquoise water and a wooden long-tail boat"></div>

  <header class="topbar">
    <div class="brand"><span class="brand-mark"></span><span class="brand-name">Brightwater</span></div>
    <div class="social"><span></span><span></span><span></span><span></span><span></span><span></span></div>
    <div class="lang">Change Language <span class="flag en"></span><span class="flag cn"></span></div>
  </header>

  <nav class="nav">
    <a href="#">HOME</a><a href="#">TOURS</a><a href="#">PAGES</a><a href="#">BLOG</a><a href="#">SHORTCODES</a><a href="#">CONTACT</a>
    <div class="auth"><a class="login" href="#">Login</a><a class="register" href="#">Register</a></div>
  </nav>

  <section class="hero">
    <div class="hero-photo" role="img" aria-label="Sydney harbour skyline with the opera house under a blue sky"></div>
    <div class="hero-banner">BRIGHTWATER<br>LEARNING TRIPS</div>
  </section>

  <section class="intro">
    <h1>BRIGHTWATER <em>LEARNING</em> TRIPS</h1>
    <p>We are passionate about educational travel and creating opportunities for students to learn more about Australia and gain a deeper understanding of its culture. The set of memorable experiences gained on our trips is invaluable. Taking the Brightwater Learning Trips tour is easy because our team of dedicated experts plans every step of the way – from enthusiastic planning of the curriculum to planning every detail of your trip to accompanying you on tour.</p>
    <p>We inspect every hotel, visit every attraction, evaluate every teacher and sample every restaurant. Wherever you go on tour, we've been there first and always listen to our travellers. We are known for our exceptional standards.</p>
    <p>We have an extensive team of specialists to help you with all your travel needs. Our team of staff have travelled around Australia and can use their first-hand knowledge to help make your trip educational, enjoyable and hassle free.</p>
    <a class="btn" href="#">Read More</a>
  </section>

  <section class="explore">
    <h2>EXPLORE THE WORLD</h2>
    <p class="lead">Find a destination that suits your interests and begin planning a journey your children will remember for years.</p>
    <div class="trips">
      <div class="trip"><div class="photo" role="img" aria-label="Mountain valley with a lake in Kazakhstan" style="background:linear-gradient(180deg,#8fc0e0,#7aa67a 60%,#4d6f4a)"></div><span class="label">Trip To Kazakhstan</span><span class="badge">$890<br>/ 7 days</span></div>
      <div class="trip"><div class="photo" role="img" aria-label="City skyline lit at night" style="background:linear-gradient(180deg,#1c2c6b,#3a4fa0 55%,#c77a3a)"></div><span class="label">20 Days From Perth</span><span class="badge">$1,290<br>/ 20 days</span></div>
      <div class="trip"><div class="photo" role="img" aria-label="Old town rooftops beside a river at dusk" style="background:linear-gradient(180deg,#3b4f8c,#7a6aa0 50%,#c49070)"></div><span class="label">Old Town Walks</span><span class="badge">$640<br>/ 5 days</span></div>
    </div>
  </section>

  <section class="offers">
    <h3>OFFER</h3>
    <span class="col-title" style="left:20px">Sponsored</span>
    <span class="col-title" style="left:268px">Special Offers</span>
    <div class="sponsored">
      <div class="photo" role="img" aria-label="Harbour city skyline on a sunny day"></div>
      <a class="btn" href="#">VIEW</a>
    </div>
    <div class="specials">
      <div class="card"><div class="thumb" role="img" aria-label="Travel merchandise on display" style="background:linear-gradient(135deg,#e9c27a,#c56a4a)"></div><h4>10% Off All Merchandise</h4><p>Enjoy savings on bags, caps and travel gear for every student joining a spring tour this year.</p><a class="btn" href="#">BOOK NOW</a></div>
      <div class="card"><div class="thumb" role="img" aria-label="Sunny beach with clear water" style="background:linear-gradient(180deg,#7cc6e6,#e6d6a6)"></div><h4>20-30% Off - Outdoor Beach</h4><p>Coastal camps with surfing lessons, marine science days and guided walks along the shore.</p><a class="btn" href="#">BOOK NOW</a></div>
      <div class="card"><div class="thumb" role="img" aria-label="Lakeside summer camp among trees" style="background:linear-gradient(180deg,#9ccfe0,#6fa06a)"></div><h4>50% Off Lakeside Summer</h4><p>Half price places on our lakeside summer program with canoeing, crafts and English classes.</p><a class="btn" href="#">BOOK NOW</a></div>
    </div>
  </section>

  <footer class="footer">
    <div class="links">
      <a href="#">HOME</a><a href="#">PLACES TO GO</a>
      <a href="#">INFORMATION</a><a href="#">EVENTS</a>
      <a href="#">THINGS TO DO</a><a href="#">TRAVEL GUIDE</a>
      <a href="#">PLACES TO STAY</a>
    </div>
    <div class="follow">
      <span class="title">Follow Us</span>
      <div class="icons"><span></span><span></span><span></span></div>
    </div>
    <div class="footer-brand"><span class="brand-mark"></span><span class="brand-name">Brightwater</span></div>
    <div class="copyright">COPYRIGHT 2015 BRIGHTWATER LEARNING TRIPS. ALL RIGHTS RESERVED</div>
    <div class="promo">
      <span class="download">FREE DOWNLOAD</span>
      <span class="item">HARBOUR STAY<small>Boutique rooms</small></span>
      <span class="item">CORAL POINT<small>Beach resort</small></span>
      <span class="item">SUMMIT LODGE<small>Mountain retreat</small></span>
    </div>
  </footer>
</div>
</body>
</html>
```